QARVELL-PRO Web Design

We are a Health, Safety, Environmental & Quality Recruitment Agency, our clients are major corporate Mining, Oil & Gas and Engineering companies. We have offices in Perth & Melbourne, Australia

The website should be very functional & easy to navigate

BUT REALLY LOOKING FOR WOW FACTOR!
Updates

Please Note: TRIVEX HOLDINGS IS OUR OLD COMPANY THE NEW ONE IS "TRIVEX-PRO" 

Some idea's from our competitors:

http://www.guardlinemerit.com.au/
http://www.wardenplacement.com.au/
http://www.keelhunt.com.au/
http://www.brqstaffing.co.uk/
http://www.laborvane.com/health-safety-environment-jobs

Would love to see some of our valued clients and there logos

still looking for wow factor

Industry/Entity Type

Mining

Requirements
Must have
• A place where candidates can upload there resumes & other contact details
• eg: http://www.guardlinemerit.com.au/candidates/register-your-resume/
• A place we can load jobs on to eg: http://www.guardlinemerit.com.au/vacancies/
• Contact details:
• Perth: 17 Brindlecombe Ave, West Perth, Western Australia 6005
• t: 08 9517 3064 | f: 08 9517 3070 |
• Melbourne: Level 1, 212 Harrowgate Street, Melbourne, Victoria 3000
• t: 03 9655 4217| f: 03 9655 4290 |
• e: dmorl@trivexpro.com.au | w: http://www.trivexpro.com.au

```html
<!DOCTYPE html>
<html lang="en">
<head>
<meta charset="utf-8">
<title>QARVELL-PRO | Health, Safety, Environmental &amp; Quality Recruitment</title>
<link rel="stylesheet" href="https://fonts.googleapis.com/css2?family=Arimo:wght@400;700&family=PT+Sans+Narrow&display=swap">
<style>
  :root{
    --slate-dark:#2f3944;
    --slate-mid:#3d4853;
    --page-bg:#efefef;
    --panel:#ffffff;
    --ink:#4a4a4a;
    --ink-soft:#6b6b6b;
    --accent-blue:#7da2c4;
    --button-blue:#a9c0d6;
    --nav-active:#4f5b66;
    --band-grey:#efefef;
    --rule:#d9d9d9;
    --logo-cyan:#2aa6d9;
  }
  *{margin:0;padding:0;box-sizing:border-box}
  html,body{width:1177px;height:1200px;overflow:hidden}
  body{position:relative;background:var(--page-bg);font-family:Arimo,Arial,sans-serif;color:var(--ink)}
  .abs{position:absolute}

  .top-band{left:0;top:0;width:1177px;height:508px;background:linear-gradient(180deg,var(--slate-mid),var(--slate-dark))}
  .social-label{left:182px;top:28px;font-size:9px;color:#cfd6dc}
  .social-icons{left:324px;top:26px;display:flex;gap:4px}
  .social-icons span{width:13px;height:13px;border-radius:2px;background:#8fa3b6;display:block}
  .search-label{left:766px;top:30px;font-size:10.5px;color:#e6eaee}
  .search-input{left:832px;top:25px;width:149px;height:21px;background:#fff;border:1px solid #c9c9c9;font-size:9px;color:#aaa;padding:5px 7px}
  .search-btn{left:981px;top:25px;width:21px;height:21px;background:#222}

  .column{left:177px;top:67px;width:825px;height:1081px;background:var(--panel)}

  .logo{left:194px;top:78px;display:flex;align-items:center;gap:12px}
  .logo-mark{width:82px;height:82px;background:var(--logo-cyan);display:block}
  .logo-name{font-size:26px;font-weight:400;color:#5a6470;letter-spacing:1px}

  .nav{left:674px;top:103px;display:flex;align-items:center;font-size:10.5px;color:var(--ink)}
  .nav .active{width:63px;height:29px;background:var(--nav-active);color:#fff;display:flex;align-items:center;justify-content:center;margin-right:12px}
  .nav .sep{margin:0 8px;color:#777}

  .hero{left:185px;top:172px;width:807px;height:336px;background:linear-gradient(160deg,#8c949a 0%,#5c6268 40%,#6b5a3a 70%,#3e4347 100%)}
  .hero-title{left:220px;top:396px;font-weight:700;font-size:25px;color:#fff;letter-spacing:-0.5px}
  .hero-text{left:220px;top:425px;width:400px;font-family:"PT Sans Narrow","Arial Narrow",sans-serif;font-size:15.5px;line-height:18px;color:#fff;text-transform:uppercase}

  .welcome-title{left:203px;top:534px;font-size:15px;font-weight:700;color:#555}
  .welcome-body{left:203px;top:572px;width:762px;font-size:9px;line-height:16.8px;color:var(--ink-soft)}
  .view-more{left:886px;top:660px;width:67px;text-align:right;font-size:8.6px;color:var(--ink-soft)}

  .jobs-band{left:195px;top:685px;width:774px;height:42px;background:var(--band-grey)}
  .jobs-title{left:212px;top:697px;font-size:15px;font-weight:700;color:#555}
  .view-all{left:885px;top:697px;width:69px;height:19px;background:var(--button-blue);color:#fff;font-size:8.6px;display:flex;align-items:center;justify-content:center}

  .job{top:751px;width:183px;font-size:8.6px;line-height:15px;color:var(--ink-soft)}
  .job-photo{width:183px;height:96px;border:4px solid #e6e6e6;margin-bottom:12px}
  .job-title{font-weight:700;color:#555}
  .job-link{color:var(--accent-blue)}

  .col-heading{top:954px;font-size:15px;font-weight:700}
  .col-heading.muted{color:#888}
  .col-heading.dark{color:#555}
  .side-photo{top:986px;width:124px;height:143px}
  .links{top:982px;list-style:none;font-size:8.6px;line-height:16.8px;color:var(--ink-soft)}
  .links li{display:flex;align-items:center;gap:6px}
  .links li::before{content:"";width:6px;height:6px;border-radius:50%;background:#333;flex:none}
  .divider{top:953px;width:1px;height:161px;background:var(--rule)}
  .select{left:496px;width:213px;height:17px;border:1px solid #9a9a9a;font-size:8.6px;color:#555;padding:3px 6px;background:#fff}
  .select::after{content:"";position:absolute;right:1px;top:1px;width:13px;height:13px;border:1px solid #777;background:linear-gradient(#fff,#ddd)}
  .select i{position:absolute;right:4px;top:6px;width:0;height:0;border-left:4px solid transparent;border-right:4px solid transparent;border-top:4px solid #333;z-index:1}
  .hint{left:498px;top:1088px;font-size:8.6px;color:#555}
  .btn{top:1110px;height:18px;background:var(--button-blue);color:#fff;font-size:9px;font-weight:700;display:flex;align-items:center;justify-content:center}

  .footer-rule{left:177px;top:1148px;width:825px;height:1px;background:#e2e2e2}
  .copyright{left:179px;top:1165px;font-size:8.6px;color:#777}
</style>
</head>
<body>
  <div class="abs top-band"></div>
  <div class="abs social-label">Follow us on the social network</div>
  <div class="abs social-icons"><span></span><span></span><span></span><span></span></div>
  <div class="abs search-label">Site Search:</div>
  <div class="abs search-input">Search</div>
  <div class="abs search-btn">
    <svg width="21" height="21" viewBox="0 0 21 21"><circle cx="9.5" cy="9.5" r="4" fill="none" stroke="#fff" stroke-width="1.6"/><line x1="12.5" y1="12.5" x2="16" y2="16" stroke="#fff" stroke-width="1.8"/></svg>
  </div>

  <div class="abs column"></div>

  <div class="abs logo"><span class="logo-mark"></span><span class="logo-name">QARVELL-PRO</span></div>

  <nav class="abs nav">
    <span class="active">Home</span>
    <span>Job Seekers</span><span class="sep">|</span>
    <span>Employers</span><span class="sep">|</span>
    <span>About us</span><span class="sep">|</span>
    <span>Contact</span>
  </nav>

  <div class="abs hero" role="img" aria-label="Large bucket-wheel excavator at an open-cut mine site"></div>
  <div class="abs hero-title">QARVELL-PRO</div>
  <div class="abs hero-text">We are a health, safety, environmental &amp; quality recruitment agency, our clients are major corpo-rate mining, oil &amp; gas and engineering companies.</div>

  <h1 class="abs welcome-title">Welcome to QARVELL-PRO</h1>
  <p class="abs welcome-body">We are a Health, Safety, Environmental &amp; Quality Recruitment Agency, our clients are major corporate Mining, Oil &amp; Gas and Engineering companies. We have offices in Perth &amp; Melbourne, Australia We are a Health, Safety, Environmental &amp; Quality Recruitment Agency, our clients are major corporate Mining, Oil &amp; Gas and Engineering companies. We have offices in Perth &amp; Melbourne, Australia We are a Health, Safety, Environmental &amp; Quality Recruitment Agency, our clients are major corporate Mining, Oil &amp; Gas and Engineering companies. We have offices in Perth &amp; Melbourne, Australia We are a Health, Safety, Environmental &amp; Quality Recruitment Agency, our clients are major corporate Mining, Oil &amp; Gas and Engineering companies. We have offices in Perth &amp; Melbourne, Australia</p>
  <div class="abs view-more">&gt;&gt; view more</div>

  <div class="abs jobs-band"></div>
  <h2 class="abs jobs-title">Latest jobs</h2>
  <div class="abs view-all">View All »</div>

  <article class="abs job" style="left:195px">
    <div class="job-photo" role="img" aria-label="Cargo ship moored at a port" style="background:linear-gradient(180deg,#6f95b8 0%,#b84a3a 55%,#1f3e7a 100%)"></div>
    <span class="job-title">First Responders Paramedics Nurses (RN EN)</span> Contract or Temp<br>Sydney<br><span class="job-link">&gt;&gt; View</span>
  </article>
  <article class="abs job" style="left:391px">
    <div class="job-photo" role="img" aria-label="Engineer on the phone in front of a refinery" style="background:linear-gradient(180deg,#a9c4de 0%,#d7dde2 50%,#6c7884 100%)"></div>
    <span class="job-title">Work Health Safety Advisor Transporta-tion and Logistics Sector</span>Permanent Full Time Sydney<br><span class="job-link">&gt;&gt; view</span>
  </article>
  <article class="abs job" style="left:588px">
    <div class="job-photo" role="img" aria-label="Yellow hard hat with safety glasses" style="border:none;background:linear-gradient(135deg,#6b5a2a 0%,#d9a92a 50%,#3b3325 100%)"></div>
    <span class="job-title">Casual Safety Advisors Shop Refur-bishment</span> Permanent Full Time<br>Sydney<br><span class="job-link">&gt;&gt; more</span>
  </article>
  <article class="abs job" style="left:785px">
    <div class="job-photo" role="img" aria-label="Supply vessel beside storage silos" style="background:linear-gradient(180deg,#8fa2b4 0%,#b9c0c4 55%,#2f5a4a 100%)"></div>
    <span class="job-title">Casual Safety Advisors Shop Refur-bishment</span> Permanent Full Time<br>Sydney<br><span class="job-link">&gt;&gt; more</span>
  </article>

  <h3 class="abs col-heading muted" style="left:206px">Job seekers</h3>
  <div class="abs side-photo" role="img" aria-label="Site worker in hard hat and high-visibility vest" style="left:206px;background:linear-gradient(180deg,#9ec3e2 0%,#d8e5ef 45%,#e8742a 75%,#d9c53a 100%)"></div>
  <ul class="abs links" style="left:346px">
    <li>Find a Job</li><li>Candidate Portal Login</li><li>Register with</li><li>Areas of Expertise</li><li>Learn New Skills</li><li>Resource Library</li><li>Our Partnerships</li>
  </ul>
  <div class="abs btn" style="left:346px;width:111px">Register with us</div>

  <div class="abs divider" style="left:472px"></div>

  <h3 class="abs col-heading dark" style="left:500px">Find a Job</h3>
  <div class="abs select" style="top:984px">Sector<i></i></div>
  <div class="abs select" style="top:1010px">Employment Area<i></i></div>
  <div class="abs select" style="top:1036px">Contract / Permanent<i></i></div>
  <div class="abs select" style="top:1062px">Salary / Pay Rate<i></i></div>
  <div class="abs hint">Please select your criteria</div>
  <div class="abs btn" style="left:489px;width:69px">View</div>
  <div class="abs btn" style="left:569px;width:68px">Advanced</div>

  <div class="abs divider" style="left:731px"></div>

  <h3 class="abs col-heading dark" style="left:754px">Employers</h3>
  <div class="abs side-photo" role="img" aria-label="Miner holding a raw metallic ore sample" style="left:754px;background:linear-gradient(135deg,#5a4a3c 0%,#a3968a 50%,#3a322c 100%)"></div>
  <ul class="abs links" style="left:887px">
    <li>Why register with us?</li><li>Submit Your CV</li><li>Interview Techniques</li><li>Refer a Friend</li><li>Employers testimonials</li><li>Get in touch</li>
  </ul>

  <div class="abs footer-rule"></div>
  <div class="abs copyright">© Copyright Qarvell Holdings Pty Ltd &nbsp;© 2008-2013 . All Rights Reserved</div>
</body>
</html>
```